Business Card Design - Service Company

Use of the card mainly in living rooms and relations b2b We wish a card with a modern design, blue tones in the background would be a plus The card must be front / back (one side with the logo / the other with the information of contact )

Font styles to use
Serif

Requirements
Must have
• Using the map on the back of the business card Editable format! Photoshop CS2 / Illustrator CS2
Nice to have
• Maquis Vertex IT Pierre Blanche Commercial Center, 20480 Lorvanu 0495718243 Siret 71384096200018 APE 6203Y https://www.fb.com/ateliertech.maquisvertex www.maquis-vertex.com

```html
<!DOCTYPE html>
<html lang="en">
<head>
<meta charset="utf-8">
<title>Maquis Vertex IT – Business Card</title>
<link rel="stylesheet" href="https://fonts.googleapis.com/css2?family=Merriweather:wght@400;700&display=swap">
<style>
  :root {
    --stage: #1f2023;
    --card-dark: #0b0b0c;
    --card-dark-2: #1a1a1c;
    --card-light: #ffffff;
    --card-light-2: #eceef0;
    --brand-blue: #2b88d0;
    --slate: #6d6e71;
    --text-grey: #5a5b5e;
    --white: #ffffff;
  }
  * { margin: 0; padding: 0; box-sizing: border-box; }
  html, body {
    width: 1200px; height: 800px; overflow: hidden;
    background: var(--stage);
    font-family: "Merriweather", Georgia, serif;
  }
  .card {
    position: absolute;
    width: 520px; height: 300px;
    overflow: hidden;
    box-shadow: 0 18px 40px rgba(0,0,0,.45);
  }
  .card-texture { position: absolute; inset: 0; }

  /* Front: logo side */
  .card-front { left: 80px; top: 110px; }
  .card-front .card-texture {
    background: linear-gradient(135deg, var(--card-dark-2), var(--card-dark) 60%);
  }
  .front-brand {
    position: absolute; inset: 0;
    display: flex; align-items: center; justify-content: center; gap: 12px;
  }
  .brand-square { width: 14px; height: 14px; background: var(--brand-blue); }
  .brand-name {
    color: var(--brand-blue);
    font-weight: 700; font-size: 30px; letter-spacing: .5px;
  }

  /* Back: contact side */
  .card-back { left: 600px; top: 390px; }
  .card-back .card-texture {
    background: linear-gradient(135deg, var(--card-light), var(--card-light-2));
  }
  .back-shapes { position: absolute; inset: 0; }
  .company {
    position: absolute; left: 92px; top: 76px;
    color: var(--brand-blue); font-weight: 700; font-size: 17px;
    text-transform: uppercase; letter-spacing: .5px;
  }
  .address {
    position: absolute; left: 92px; top: 102px;
    color: var(--text-grey); font-size: 11px;
  }
  .person { position: absolute; left: 140px; top: 160px; color: var(--white); }
  .person-name { font-weight: 700; font-size: 15px; text-transform: uppercase; }
  .person-role { font-size: 11px; margin-top: 1px; }
  .contact-list {
    position: absolute; left: 140px; top: 200px; list-style: none;
    color: var(--white); font-size: 11px;
  }
  .contact-list li { display: flex; align-items: center; gap: 8px; height: 16px; }
  .contact-icon { width: 12px; height: 12px; flex: none; }
  .legal {
    position: absolute; left: 140px; top: 266px;
    color: var(--text-grey); font-size: 11px;
  }
</style>
</head>
<body>

<section class="card card-front" aria-label="Card front">
  <div class="card-texture" role="img" aria-label="Dark faceted diamond texture"></div>
  <div class="front-brand">
    <span class="brand-square"></span>
    <span class="brand-name">Maquis Vertex IT</span>
  </div>
</section>

<section class="card card-back" aria-label="Card back">
  <div class="card-texture" role="img" aria-label="Light faceted diamond texture"></div>
  <svg class="back-shapes" width="520" height="300" viewBox="0 0 520 300" aria-hidden="true">
    <polygon points="60,168 88,168 110,188 110,252 60,252" fill="var(--slate)"/>
    <polygon points="92,148 520,148 520,252 122,252 122,184 92,160" fill="var(--brand-blue)"/>
  </svg>

  <div class="company">Maquis Vertex IT</div>
  <div class="address">Pierre Blanche Commercial Center, 20480 Lorvanu</div>

  <div class="person">
    <div class="person-name">Paul Santoni</div>
    <div class="person-role">Director</div>
  </div>

  <ul class="contact-list">
    <li>
      <svg class="contact-icon" viewBox="0 0 12 12" aria-hidden="true">
        <circle cx="6" cy="6" r="5.5" fill="none" stroke="#fff"/>
        <path d="M4 3.2 L5 4.6 L4.5 5.3 Q5.2 6.8 6.7 7.5 L7.4 7 L8.8 8 L8.2 9 Q5 8.8 3.2 4 Z" fill="#fff"/>
      </svg>
      0495718243
    </li>
    <li>
      <svg class="contact-icon" viewBox="0 0 12 12" aria-hidden="true">
        <circle cx="6" cy="6" r="5.5" fill="none" stroke="#fff"/>
      </svg>
      ateliertech.maquisvertex
    </li>
    <li>
      <svg class="contact-icon" viewBox="0 0 12 12" aria-hidden="true">
        <circle cx="6" cy="6" r="5.5" fill="none" stroke="#fff"/>
        <circle cx="6" cy="6" r="2.5" fill="none" stroke="#fff"/>
      </svg>
      www.maquis-vertex.com
    </li>
  </ul>

  <div class="legal">Siret 71384096200018 APE 6203Y</div>
</section>

</body>
</html>
```